Web Design Project

I have a website which looks dull and uninteresting. I'd like to apply a fresh and clean look to it, which better reflects the quality of the service I sell.The website address is http://www.brightquillpages.co.uk.

Target Market(s)

Financial advisers (financially sophisticated individuals)

Industry/Entity Type

It Service

Requirements
Should not have
• Please do not use obvious but irrelevant and boring imagery such as banks, pages from the DL, money, books or libraries. Prefer slick relevant graphics and crisp typography.

```html
<!DOCTYPE html>
<html lang="en">
<head>
<meta charset="utf-8">
<title>Contact us – BrightQuillPages.co.uk</title>
<link rel="stylesheet" href="https://fonts.googleapis.com/css2?family=Arimo:ital,wght@0,400;0,700;1,400&family=Varela+Round&display=swap">
<style>
:root{
  --band:#e6e7e8;
  --orange:#f26a1b;
  --red:#ee3a3a;
  --olive:#8a866f;
  --olive-dark:#7d7a66;
  --ink:#111;
  --muted:#8d8d8d;
  --footer:#5f5f61;
  --field-border:#d9d9d9;
  --field-bg:#fdfdfd;
}
*{box-sizing:border-box;margin:0;padding:0}
html,body{width:1200px;height:900px;overflow:hidden;background:#fff}
body{position:relative;font-family:"Arimo",Arial,sans-serif;color:var(--ink)}
.abs{position:absolute}

.topbar{left:0;top:0;width:1200px;height:37px;background:var(--band);font-size:12px;letter-spacing:.6px;color:#444}
.topbar .date{position:absolute;left:232px;top:16px}
.topbar .utility{position:absolute;right:220px;top:16px;word-spacing:2px}

.brand{left:221px;top:64px;display:flex;align-items:center;gap:10px}
.brand-mark{width:44px;height:44px;border-radius:9px;background:var(--orange)}
.brand-name{font-size:30px;font-weight:700;color:var(--olive-dark);letter-spacing:-.3px}
.tagline{left:390px;top:104px;font-size:11px;color:#222}

.login-label{left:720px;top:72px;width:58px;text-align:right;font-size:11px;line-height:14px;color:#333}
.login-input{left:789px;width:190px;height:24px;border:1px solid #ccc;background:#fff;font-size:9.5px;font-style:italic;color:#aaa;padding:6px 7px}
.forgot{left:790px;top:119px;font-size:9.5px;font-style:italic;color:#444;letter-spacing:.5px}
.login-btn{left:932px;top:115px;width:47px;height:18px;border:1px solid #555;border-radius:4px;background:linear-gradient(#fafafa,#d8d8d8);font-size:11px;text-align:center;line-height:16px;color:#222}

.nav{left:221px;top:159px;width:758px;height:26px}
.nav-tab{position:absolute;top:0;height:26px;background:var(--band);border-radius:7px 7px 0 0;font-size:12px;color:#222;text-align:center;line-height:31px}
.nav-tab.active{background:var(--orange);color:#fff;line-height:28px}

.page-title{left:306px;top:210px;font-family:"Varela Round",Arial,sans-serif;font-size:25px;color:var(--red)}
.call-line{left:308px;top:247px;font-size:14px}
.call-line .phone{color:var(--red)}

.form-title{left:450px;top:296px;font-size:26px}
.field-label{left:313px;font-size:12.5px}
.field{left:449px;width:236px;border:1px solid var(--field-border);background:var(--field-bg)}
.select{font-size:12.5px;padding:7px 8px}
.select-arrow{position:absolute;right:0;top:0;width:22px;height:100%;background:linear-gradient(#b5b5b5,#8a8a8a);color:#333;font-size:12px;text-align:center;line-height:26px}
.field-note{left:452px;top:577px;width:240px;font-size:10px;line-height:13px}
.btn{top:612px;height:26px;border:1px solid #555;border-radius:7px;background:linear-gradient(#f3f3f3,#a9a9a9);font-size:14px;text-align:center;line-height:24px;color:#222}

.sidebar-rule{left:804px;top:245px;height:306px;border-left:1px dotted #666}
.sidebar{left:819px;top:245px;list-style:none;font-size:10px;color:var(--olive);line-height:20.35px}
.social{left:824px;top:517px}

.bottom-links{left:245px;top:719px;font-size:13px;color:var(--olive);letter-spacing:.6px;word-spacing:2px}
.related{left:0;top:756px;width:1200px;height:49px;background:var(--band);font-size:13px;color:var(--muted);text-align:center;line-height:55px}
.site-footer{left:0;top:805px;width:1200px;height:95px;background:var(--footer);text-align:center}
.site-footer .links{margin-top:16px;font-size:14px;color:#fff}
.site-footer .copy{margin-top:6px;font-size:13px;color:#a0a0a0}
</style>
</head>
<body>

<header>
  <div class="abs topbar">
    <span class="date">Tuesday, August 23, 2011 &nbsp;&nbsp;&nbsp;&nbsp;&nbsp; 2:19</span>
    <span class="utility">Support &nbsp;|&nbsp;&nbsp; FAQ &nbsp;&nbsp;|&nbsp; Sitemap</span>
  </div>

  <div class="abs brand">
    <span class="brand-mark"></span>
    <span class="brand-name">BrightQuillPages.co.uk</span>
  </div>
  <div class="abs tagline">Words to use as you please</div>

  <div class="abs login-label">Member<br>Login</div>
  <div class="abs login-input" style="top:58px">Username</div>
  <div class="abs login-input" style="top:85px">Password</div>
  <div class="abs forgot">Forgotten your password?</div>
  <div class="abs login-btn">Login</div>

  <nav class="abs nav">
    <span class="nav-tab" style="left:0;width:90px">Home</span>
    <span class="nav-tab active" style="left:92px;width:88px">A-Z Articles</span>
    <span class="nav-tab" style="left:183px;width:104px">Inheritance Tax</span>
    <span class="nav-tab" style="left:290px;width:84px">Insurances</span>
    <span class="nav-tab" style="left:378px;width:85px">Mortgages</span>
    <span class="nav-tab" style="left:467px;width:57px">Other</span>
    <span class="nav-tab" style="left:527px;width:86px">Retirement</span>
    <span class="nav-tab" style="left:617px;width:141px">Saving &amp; Investment</span>
  </nav>
</header>

<main>
  <h1 class="abs page-title">Contact us:</h1>
  <p class="abs call-line">If you'd prefer to call us, please call <span class="phone">07700 900461.</span></p>

  <h2 class="abs form-title" style="font-weight:400">Email Us</h2>

  <div class="abs field-label" style="top:346px">Name:*</div>
  <div class="abs field" style="top:339px;height:27px"></div>

  <div class="abs field-label" style="top:380px">Email Address:*</div>
  <div class="abs field" style="top:373px;height:27px"></div>

  <div class="abs field-label" style="top:415px">Nature of Enquiry</div>
  <div class="abs field select" style="top:408px;height:27px">Free IHT guide<span class="select-arrow">V</span></div>

  <div class="abs field-label" style="top:449px">Comment or Question</div>
  <div class="abs field" style="top:443px;height:92px"></div>

  <div class="abs field-label" style="top:549px">Phone Number</div>
  <div class="abs field" style="top:543px;height:27px"></div>
  <p class="abs field-note">If you would prefer us to call you, please provide a telephone number.</p>

  <div class="abs btn" style="left:560px;width:51px">Reset</div>
  <div class="abs btn" style="left:622px;width:51px">Send</div>

  <aside>
    <div class="abs sidebar-rule"></div>
    <ul class="abs sidebar">
      <li>Home</li>
      <li>Samples</li>
      <li>The people who write the articles</li>
      <li>Please don't lift our words</li>
      <li>A - Z of articles</li>
      <li>Enter the library</li>
      <li>Join the library here</li>
      <li>Some FAQs</li>
      <li>Contact us</li>
      <li>A few terms &amp; conditions</li>
      <li>A comment to make?</li>
      <li>A question to ask?</li>
      <li>Want something writing?</li>
    </ul>
    <svg class="abs social" width="92" height="26" viewBox="0 0 92 26" role="img" aria-label="Social links">
      <defs>
        <radialGradient id="socialDot" cx="40%" cy="35%" r="70%">
          <stop offset="0" stop-color="#8a8a8a"/>
          <stop offset="1" stop-color="#333"/>
        </radialGradient>
      </defs>
      <circle cx="12" cy="13" r="12" fill="url(#socialDot)"/>
      <circle cx="45" cy="13" r="12" fill="url(#socialDot)"/>
      <circle cx="78" cy="13" r="12" fill="url(#socialDot)"/>
    </svg>
  </aside>

  <p class="abs bottom-links">View our library &nbsp;|&nbsp;&nbsp; See samples of our articles</p>
</main>

<footer>
  <div class="abs related">Why financial advice can never be free &nbsp;|&nbsp; What it takes to be a financial adviser &nbsp;|&nbsp; IHT Planning: A guessing and waiting game...</div>
  <div class="abs site-footer">
    <p class="links">Home &nbsp;|&nbsp; A - Z Articles &nbsp;|&nbsp; Inheritance Tax &nbsp;|&nbsp; Insurances &nbsp;| Mortgages &nbsp;|&nbsp; Other &nbsp;|&nbsp; Retirement &nbsp;|&nbsp; Saving and Investment</p>
    <p class="copy">© 2011 &nbsp;All rights reserved. &nbsp;BrightQuillPages.co.uk</p>
  </div>
</footer>

</body>
</html>
```